Business card for new consulting business - Brackenvale Enterprises Pty Ltd.

Consulting in the areas of Occupational Health, Safety and Community Relations in the resources (mining) industries. The consultant (me) will work both within Australia and overseas jurisdictions such as South East Asia, Africa , South America etc, often working with third world indigenous communities. The design should suggest a high level of social and environmental responsibility.

```html
<!DOCTYPE html>
<html lang="en">
<head>
<meta charset="utf-8">
<title>Brackenvale Enterprises Pty Ltd – Business Card</title>
<link href="https://fonts.googleapis.com/css2?family=Lato:wght@300;400;700&display=swap" rel="stylesheet">
<style>
  :root {
    --bg: #2b2b2b;
    --brown: #6a4016;
    --brown-deep: #55330f;
    --brown-ink: #5b3612;
    --gold: #e8ad2c;
    --paper: #f6f5f3;
    --paper-shade: #e9e8e6;
    --ink: #1f1f1f;
    --white: #ffffff;
  }
  * { margin: 0; padding: 0; box-sizing: border-box; }
  html, body {
    width: 1200px;
    height: 900px;
    overflow: hidden;
    background: var(--bg);
    font-family: "Lato", sans-serif;
  }
  .canvas {
    position: relative;
    width: 1200px;
    height: 900px;
  }
  .card {
    position: absolute;
    width: 560px;
    height: 320px;
    border-radius: 28px;
    box-shadow: 0 18px 40px rgba(0,0,0,0.55);
  }
  /* Front */
  .card-front {
    left: 80px;
    top: 110px;
    background: linear-gradient(160deg, var(--brown) 0%, var(--brown-deep) 100%);
    display: flex;
    align-items: center;
    justify-content: center;
  }
  .brand {
    display: flex;
    flex-direction: column;
    align-items: center;
  }
  .brand-square {
    width: 112px;
    height: 78px;
    background: var(--gold);
    margin-bottom: 14px;
  }
  .brand-name {
    font-weight: 300;
    font-size: 40px;
    letter-spacing: 2px;
    text-transform: uppercase;
    line-height: 1;
  }
  .brand-tagline {
    margin-top: 8px;
    font-weight: 400;
    font-size: 10.5px;
    letter-spacing: 4px;
    text-transform: uppercase;
    color: var(--gold);
  }
  .card-front .brand-name { color: var(--white); }

  /* Back */
  .card-back {
    left: 560px;
    top: 470px;
    background: radial-gradient(ellipse at 70% 20%, var(--paper) 0%, var(--paper) 45%, var(--paper-shade) 100%);
    display: flex;
    align-items: center;
    padding: 0 40px 0 44px;
    gap: 30px;
  }
  .card-back .brand-square { width: 84px; height: 58px; margin-bottom: 10px; }
  .card-back .brand-name { color: var(--brown-ink); font-size: 28px; letter-spacing: 1.5px; }
  .card-back .brand-tagline { font-size: 7.5px; letter-spacing: 3px; margin-top: 6px; }

  .contact { margin-left: auto; }
  .person-name {
    font-weight: 400;
    font-size: 22px;
    color: var(--ink);
  }
  .person-title {
    font-size: 14px;
    color: var(--gold);
    margin-bottom: 16px;
  }
  .contact-list { list-style: none; }
  .contact-item {
    display: flex;
    align-items: center;
    gap: 8px;
    font-size: 14px;
    color: var(--ink);
    margin-bottom: 6px;
  }
  .contact-icon { width: 13px; height: 13px; flex: none; }
</style>
</head>
<body>
<main class="canvas">

  <section class="card card-front" aria-label="Card front">
    <div class="brand">
      <div class="brand-square"></div>
      <div class="brand-name">Brackenvale</div>
      <div class="brand-tagline">Enterprises Pty Ltd.</div>
    </div>
  </section>

  <section class="card card-back" aria-label="Card back">
    <div class="brand">
      <div class="brand-square"></div>
      <div class="brand-name">Brackenvale</div>
      <div class="brand-tagline">Enterprises Pty Ltd.</div>
    </div>

    <div class="contact">
      <div class="person-name">Your Name</div>
      <div class="person-title">Job Title</div>
      <ul class="contact-list">
        <li class="contact-item">
          <svg class="contact-icon" viewBox="0 0 16 16" aria-hidden="true">
            <path fill="#5b3612" d="M1 5c0-2 3-3 7-3s7 1 7 3v1h-4V5H5v1H1z"/>
            <rect x="3" y="7" width="10" height="7" rx="1" fill="#5b3612"/>
            <circle cx="8" cy="10.5" r="1.6" fill="#f6f5f3"/>
          </svg>
          000 000 0000
        </li>
        <li class="contact-item">
          <svg class="contact-icon" viewBox="0 0 16 16" aria-hidden="true">
            <rect x="1" y="3" width="14" height="10" fill="#5b3612"/>
            <path d="M1 3l7 6 7-6" fill="none" stroke="#f6f5f3" stroke-width="1.3"/>
          </svg>
          youremail@xyz.com
        </li>
        <li class="contact-item">
          <svg class="contact-icon" viewBox="0 0 16 16" aria-hidden="true">
            <g fill="none" stroke="#5b3612" stroke-width="1.3">
              <circle cx="8" cy="8" r="6.5"/>
              <ellipse cx="8" cy="8" rx="3" ry="6.5"/>
              <path d="M1.5 8h13M3 4.5h10M3 11.5h10"/>
            </g>
          </svg>
          www.website.com
        </li>
      </ul>
    </div>
  </section>

</main>
</body>
</html>
```